BRIGHTWELL PARTNERS POWERPOINT PRESENTATION TEMPLATE 1

We need the ultimate quality Powerpoint presentation design.
We are the advisory firm working with modern world class tech companies throughout Europe, their founders, shareholders, and potential investors.
The new template must contain elements such as our logo, appropriate backgrounds, be at the same time very attractive visually and easy to rear. Also there must be some place where logo of our clients should be placed.

We like:
- icons and
- infographics,
so attractive design in this area will be greatly appreciated.

Please avoid serif fonts and excessive decorations such as "waves" or other similar decor.

We are also in contact with serious investors - wealthy individuals, reputable financial institutions, and their advisers; banks, private equity investors, global technology companies.

The Powerpoint template design must send a message that:
- we are a high technology oriented team of professionals,
- we provide modern financial advisory services
- but at the same time we are open minded, creative, yet very competent in the area of corporate finance.

The Powerpoint template must complement our business card design, first impression of a team of top notch professionals who advise top notch tech companies on their top notch corporate finance and M&A projects.

Enclosed are sets of our logo, current template, business card project which won previous competition.

It is perhaps a good basis to start with and get us to the template of our dreams.

While working on this project please think about the following firms which at some point may be looking at your design:
- Quorra
- Veltrix
- Pondero
- Zentaro (Brixel)
- Moodlane
- Kurotan
- Wavoro
- Dalvion
- Strelo

The quality of the design, its style, aesthetics must meet the top criteria in contemporary design trends.

Target Market(s)

Banks, financial investors, strategic investors

Industry/Entity Type

Finance

Font styles to use
Sans Serif

Requirements
Must have
• Icons
Infographics
Attractive backgrounds
Clean design
Harmonize with logo and emblem colors.
Should not have
• Excessive tacky decor (waves, etc)
Serif fonts
Excessive colors

```html
<!DOCTYPE html>
<html lang="en">
<head>
<meta charset="utf-8">
<title>Brightwell Partners – Presentation Template</title>
<link href="https://fonts.googleapis.com/css2?family=Roboto:ital,wght@0,400;0,500;0,700;1,400;1,500;1,700&display=swap" rel="stylesheet">
<style>
  :root {
    --ink: #0d2a52;
    --text: #222;
    --muted: #5a5f66;
    --band: #d3e3f3;
    --band-grey: #e6ebf2;
    --rule: #7a9fd9;
    --rule-soft: #9bb6df;
    --pill: #6a86a6;
    --pill-dark: #55708f;
    --card: #dde6f5;
    --thumb: #efefef;
    --accent: #f59a23;
    --brand: #1d5fc4;
    --frame: #cfcfcf;
  }
  * { box-sizing: border-box; margin: 0; padding: 0; }
  html, body { width: 1200px; height: 1200px; overflow: hidden; background: #fff; }
  body { position: relative; font-family: "Roboto", Arial, sans-serif; color: var(--text); }
  .slide { position: absolute; background: #fff; border: 1.5px solid var(--frame); overflow: hidden; }
  .abs { position: absolute; }

  .slide--cover { left: 211px; top: 25px; width: 669px; height: 376px; }
  .slide--kpi { left: 94px; top: 420px; width: 630px; height: 354px; }
  .slide--map { left: 450px; top: 791px; width: 616px; height: 348px; }

  .cover-box { left: 118px; top: 114px; width: 413px; height: 134px; background: var(--band); }
  .cover-copy { left: 145px; top: 126px; width: 250px; font-size: 13.4px; line-height: 15.4px; font-style: italic; color: #111; }
  .cover-copy p + p { margin-top: 15px; }
  .client-logo { left: 418px; top: 140px; width: 90px; text-align: center; }
  .client-logo .mark { width: 52px; height: 52px; margin: 0 auto 12px; background: #4f87e6; }
  .client-logo .name { font-size: 12px; font-weight: 700; color: var(--accent); letter-spacing: .3px; }
  .cover-date { right: 138px; top: 254px; font-size: 10.5px; font-style: italic; }
  .rule-v { width: 1px; background: var(--rule); }
  .rule-h { height: 1px; background: var(--rule-soft); }

  .confidential { font-size: 5.8px; font-weight: 700; font-style: italic; }
  .brand { display: flex; flex-direction: column; align-items: center; gap: 3px; }
  .brand .dot { width: 15px; height: 15px; border-radius: 50%; background: var(--brand); }
  .brand .word { font-size: 11.5px; color: var(--ink); letter-spacing: -.2px; }

  .band-grey { background: var(--band-grey); }
  .band-blue { background: var(--band); }
  .slide-title { font-size: 28px; font-weight: 500; color: var(--ink); }
  .section-head { font-size: 8px; font-weight: 700; color: var(--ink); }

  .facts { font-size: 8.4px; font-weight: 500; color: var(--muted); line-height: 10.2px; }
  .fact-line { height: 1px; background: var(--rule-soft); }
  .pie-note { font-size: 4.6px; color: var(--muted); line-height: 6px; }
  .pie-tag { font-size: 3.4px; color: #888; }

  .sub-head { font-size: 8.4px; font-weight: 500; color: #111; }
  .bullets { list-style: none; }
  .bullets li { position: relative; }
  .bullets li::before { content: "→"; position: absolute; font-weight: 700; }
  .bullets--overview { left: 125px; top: 221px; width: 170px; font-size: 6.4px; line-height: 8.2px; }
  .bullets--overview li { margin-bottom: 1px; }
  .bullets--overview li::before { left: -19px; }
  .bullets--invest { left: 122px; top: 214px; width: 290px; font-size: 5.4px; line-height: 8.3px; }
  .bullets--invest li::before { left: -18px; }

  .kpi { left: 313px; width: 128px; height: 24px; border-radius: 12px; background: linear-gradient(90deg, var(--pill) 0%, var(--pill-dark) 100%); display: flex; align-items: center; color: #fff; }
  .kpi .ring { width: 21px; height: 21px; border-radius: 50%; background: #fff; border: 2px solid #cfdcec; margin-left: 2px; flex: none; }
  .kpi .value { width: 32px; text-align: center; font-size: 10px; font-weight: 700; flex: none; }
  .kpi .label { font-size: 6.2px; font-weight: 700; line-height: 9px; }

  .usp { left: 464px; width: 143px; height: 54px; background: var(--card); display: flex; }
  .usp .thumb { width: 47px; height: 100%; background: var(--thumb); border: 1px solid #777; flex: none; }
  .usp .body { padding: 4px 0 0 6px; font-size: 7.2px; line-height: 9px; color: var(--muted); }
  .usp .body b { display: block; font-weight: 500; color: #444; }

  .map { left: 334px; top: 74px; width: 256px; height: 150px; background: linear-gradient(160deg, #4cb897 0%, #5dbb9c 55%, #b9bcbf 100%); border-radius: 40% 45% 35% 30% / 45% 40% 50% 40%; opacity: .9; }
  .legend { left: 490px; top: 236px; font-size: 5.4px; font-weight: 500; line-height: 10.5px; }
  .legend span { display: inline-block; width: 5px; height: 5px; margin-right: 5px; vertical-align: middle; }
</style>
</head>
<body>

<!-- Cover slide -->
<section class="slide slide--cover">
  <div class="abs rule-v" style="left:537px; top:34px; height:269px;"></div>
  <div class="abs rule-h" style="left:371px; top:107px; width:209px; background:var(--rule);"></div>
  <div class="abs cover-box"></div>
  <div class="abs cover-copy">
    <p>Lorem ipsum <b>dolor sit amet</b>, consectetur adipiscing elit. Proin justo dui, elementum sed volutpat at, varius at nisl. Vestibulum sed aliquam tellus.</p>
    <p>Donec imperdiet lacus sed nunc efficitur, eget varius libero consequat.</p>
  </div>
  <div class="abs client-logo">
    <div class="mark"></div>
    <div class="name">COMPANY LOGO</div>
  </div>
  <div class="abs cover-date">September, 2020</div>
  <div class="abs rule-h" style="left:56px; top:336px; width:526px;"></div>
  <div class="abs confidential" style="left:64px; top:345px;">Strictly confidential</div>
  <div class="abs brand" style="left:564px; top:329px;"><div class="dot"></div><div class="word">BRIGHTWELL</div></div>
</section>

<!-- Introduction with KPIs -->
<section class="slide slide--kpi">
  <div class="abs band-grey" style="left:0; top:0; width:67px; height:64px;"></div>
  <div class="abs band-blue" style="left:67px; top:0; width:332px; height:46px;"></div>
  <div class="abs slide-title" style="left:92px; top:10px;">Introduction</div>
  <div class="abs band-blue" style="left:309px; top:34px; width:321px; height:34px;"></div>
  <div class="abs section-head" style="left:321px; top:54px;">KPIs</div>
  <div class="abs section-head" style="left:467px; top:54px;">Market Opportunities/USPs</div>
  <div class="abs rule-v" style="left:301px; top:52px; height:247px;"></div>
  <div class="abs rule-v" style="left:451px; top:14px; height:285px;"></div>

  <div class="abs facts" style="left:94px; top:68px; width:198px;">Headquarters : 1234 Lorem ipsum, dolor sit amet consectetur, adipiscing elit. 123456-789 ELEME</div>
  <div class="abs fact-line" style="left:94px; top:91px; width:198px;"></div>
  <div class="abs facts" style="left:94px; top:95px;">Industry : Lorem ipsum, dolor</div>
  <div class="abs fact-line" style="left:94px; top:108px; width:198px;"></div>
  <div class="abs facts" style="left:94px; top:113px;">Headcount : 3000+</div>
  <div class="abs fact-line" style="left:94px; top:126px; width:198px;"></div>
  <div class="abs facts" style="left:94px; top:132px;">Ownership Structure :</div>
  <div class="abs pie-note" style="left:94px; top:147px;">Lorem ipsum,<br>Dolor sit amet<br>Consectetur, adipiscing</div>
  <svg class="abs" style="left:196px; top:127px;" width="80" height="50" viewBox="-40 -25 80 50" role="img" aria-label="Ownership pie chart">
    <path d="M0,0 L0,-22 A22,22 0 1,1 -1.38,21.96 Z" fill="#000"/>
    <path d="M0,0 L-1.38,21.96 A22,22 0 0,1 -21.96,-1.38 Z" fill="#8e8e8e"/>
    <path d="M0,0 L-21.96,-1.38 A22,22 0 0,1 0,-22 Z" fill="#d8d8d8"/>
    <text class="pie-tag" x="-38" y="-17">Owner A</text>
    <text class="pie-tag" x="24" y="1">Owner B</text>
    <text class="pie-tag" x="-38" y="17">Owner C</text>
  </svg>
  <div class="abs fact-line" style="left:94px; top:182px; width:198px;"></div>
  <div class="abs sub-head" style="left:94px; top:200px;">Company Overview</div>
  <ul class="abs bullets bullets--overview">
    <li>XXX is a manufacturer of high quality products A, B, C etc..</li>
    <li>Planned tripling of revenues and quadrupling of EBITDA over [x] years</li>
    <li>The development strategy assumes introducing new product lines and expansion into foreign markets XXX</li>
    <li>The company has a unique business model based on the…</li>
  </ul>

  <div class="abs kpi" style="top:83px;"><div class="ring"></div><div class="value">12%</div><div class="label">Increase in Revenue</div></div>
  <div class="abs kpi" style="top:109px;"><div class="ring"></div><div class="value">8%</div><div class="label">Increase in<br>Production Volume</div></div>
  <div class="abs kpi" style="top:135px;"><div class="ring"></div><div class="value">20%</div><div class="label">Increase in Number<br>of Products</div></div>
  <div class="abs kpi" style="top:161px;"><div class="ring"></div><div class="value">25%</div><div class="label">Increase in<br>Production Plants</div></div>
  <div class="abs kpi" style="top:186px;"><div class="ring"></div><div class="value">40%</div><div class="label">Increase in Contract<br>Execution</div></div>
  <div class="abs kpi" style="top:212px;"><div class="ring"></div><div class="value">25%</div><div class="label">Increase in Number<br>of Employees</div></div>
  <div class="abs kpi" style="top:238px;"><div class="ring"></div><div class="value">15%</div><div class="label">Increase in Number<br>of Retailers</div></div>

  <div class="abs usp" style="top:83px;"><div class="thumb"></div><div class="body"><b>Lorem ipsum, dolor</b>Sit amet consectetur, adipiscing elit. Lorem ipsum, dolor sit amet consectetur.</div></div>
  <div class="abs usp" style="top:145px;"><div class="thumb"></div><div class="body"><b>Lorem ipsum, dolor</b>Sit amet consectetur, adipiscing elit. Lorem ipsum, dolor sit.</div></div>
  <div class="abs usp" style="top:208px;"><div class="thumb"></div><div class="body"><b>Lorem ipsum, dolor</b>Sit amet consectetur, adipiscing elit. Lorem ipsum, dolor.</div></div>

  <div class="abs rule-h" style="left:51px; top:317px; width:499px;"></div>
  <div class="abs confidential" style="left:59px; top:325px;">Strictly confidential</div>
  <div class="abs brand" style="left:532px; top:311px;"><div class="dot"></div><div class="word">BRIGHTWELL</div></div>
</section>

<!-- Introduction with coverage -->
<section class="slide slide--map">
  <div class="abs band-grey" style="left:0; top:0; width:66px; height:64px;"></div>
  <div class="abs band-blue" style="left:66px; top:0; width:324px; height:45px;"></div>
  <div class="abs slide-title" style="left:90px; top:10px;">Introduction</div>
  <div class="abs band-blue" style="left:302px; top:34px; width:314px; height:34px;"></div>
  <div class="abs section-head" style="left:314px; top:53px;">Headquarter and Geographical Coverage</div>
  <div class="abs rule-v" style="left:294px; top:51px; height:158px;"></div>

  <div class="abs facts" style="left:92px; top:67px; width:192px;">Headquarters : 1234 Lorem ipsum, dolor sit amet consectetur, adipiscing elit. 123456-789 ELEME</div>
  <div class="abs fact-line" style="left:92px; top:89px; width:192px;"></div>
  <div class="abs facts" style="left:92px; top:93px;">Industry : Lorem ipsum, dolor</div>
  <div class="abs fact-line" style="left:92px; top:106px; width:192px;"></div>
  <div class="abs facts" style="left:92px; top:110px;">Headcount : 3000+</div>
  <div class="abs fact-line" style="left:92px; top:123px; width:192px;"></div>
  <div class="abs facts" style="left:92px; top:128px;">Ownership Structure :</div>
  <div class="abs pie-note" style="left:92px; top:145px;">Lorem ipsum, 51%<br>Dolor sit amet, 25%<br>Consectetur, adipiscing, 24%</div>
  <svg class="abs" style="left:191px; top:124px;" width="80" height="50" viewBox="-40 -25 80 50" role="img" aria-label="Ownership pie chart">
    <path d="M0,0 L0,-22 A22,22 0 1,1 -1.38,21.96 Z" fill="#000"/>
    <path d="M0,0 L-1.38,21.96 A22,22 0 0,1 -21.96,-1.38 Z" fill="#8e8e8e"/>
    <path d="M0,0 L-21.96,-1.38 A22,22 0 0,1 0,-22 Z" fill="#d8d8d8"/>
    <text class="pie-tag" x="-38" y="-17">Owner A</text>
    <text class="pie-tag" x="24" y="1">Owner B</text>
    <text class="pie-tag" x="-38" y="17">Owner C</text>
  </svg>
  <div class="abs fact-line" style="left:92px; top:178px; width:192px;"></div>
  <div class="abs sub-head" style="left:92px; top:195px;">Investment Attractiveness</div>
  <ul class="abs bullets bullets--invest">
    <li>Manufacturer of high quality product A, B, C etc.</li>
    <li>One of the widest product offers on the market; production [...]</li>
    <li>Order execution on average [xx,xx]% faster than market competition</li>
    <li>Planned tripling of revenues and quadruple increase in EBITDA over [x] years</li>
    <li>Absorbent market: estimated increase in the value of the market [...] in Poland between 2018 and 2024P from [x,xx] billion PLN to [x,xx] billion PLN (CAGR x,xx%) and increase in the value of the market [...] in Poland between 2018 and 2024P from [x,xx] billion PLN to [x,xx] billion PLN (CAGR [x,xx]%)</li>
    <li>High specialization and flexibility of production based on own machinery and specialized staff</li>
    <li>Unique business model based on [...]</li>
    <li>Development strategy assuming [...]</li>
  </ul>

  <div class="abs map" role="img" aria-label="World map showing geographical spread, headquarters and production plant locations"></div>
  <div class="abs legend">
    <div><span style="background:#3fb08b;"></span>Geographical Spread</div>
    <div><span style="background:#0d2a52; border-radius:50%;"></span>Headquarters</div>
    <div><span style="background:#1d5fe0; border-radius:50%;"></span>Production plants</div>
  </div>

  <div class="abs rule-h" style="left:51px; top:309px; width:485px;"></div>
  <div class="abs confidential" style="left:59px; top:318px;">Strictly confidential</div>
  <div class="abs brand" style="left:520px; top:302px;"><div class="dot"></div><div class="word">BRIGHTWELL</div></div>
</section>

</body>
</html>
```